Postcard Design Project

script called A Lantern Under Frozen Water based on a true story and a book by the same author. It needs to have the Caldwick Pines Film Festival logo and my contact info. doreen.makepeace@quillvanemail.org and phone: 417-555-0192, the logline and the synopsis on the back of the card. Below my photo: Doreen Makepeace is a script writer with shares in two Halloran Prizes, a published book, a Wexcombe and other awards. Should have a large headline over the booking photo: A Lantern Under Frozen Water, feature film/drama based on a true story
Updates

I don't see where you added my web site. It should be on the front by the phone. www.doreenmakepeace.com

Target Market(s)

producers and agents looking for scripts

Industry/Entity Type

Movie Production

Font styles to use
Serif

Requirements
Must have
• www.doreenmakepeace.com doreen.makepeace@quillvanemail.org
• logline (included in the file attached), photo of the boy, author biographical infor., contact information and web site. Caldwick pines Film Festival logo can be downloaded from http://caldwickpinesfilmfestival.com/festival-rules/ I need the logo that says "official selection" at the top
Nice to have
• head shot of the author, doreen makepeace

```html
<!DOCTYPE html>
<html lang="en">
<head>
<meta charset="utf-8">
<title>A Lantern Under Frozen Water – Postcard Back</title>
<link rel="stylesheet" href="https://fonts.googleapis.com/css2?family=Nunito:wght@700;800&family=Nunito+Sans:wght@400;600;700&display=swap">
<style>
  :root {
    --slate-dark: #36454a;
    --slate-mid: #56676b;
    --slate-light: #6d7d80;
    --panel: rgba(38, 50, 54, 0.55);
    --gold: #c9a85a;
    --ink-light: #e6ecec;
    --logline: #c6d2d5;
    --white: #ffffff;
    --box-border: #2b2b2b;
    --box-ink: #1c1c1c;
  }
  * { margin: 0; padding: 0; box-sizing: border-box; }
  html, body { width: 1200px; height: 534px; overflow: hidden; background: #fff; }
  .postcard {
    position: relative;
    width: 1200px; height: 534px;
    overflow: hidden;
    font-family: "Nunito Sans", Arial, sans-serif;
    background:
      radial-gradient(ellipse at 70% 20%, var(--slate-light) 0%, transparent 55%),
      radial-gradient(ellipse at 20% 80%, var(--slate-mid) 0%, transparent 60%),
      linear-gradient(135deg, var(--slate-dark), var(--slate-mid) 55%, var(--slate-dark));
  }
  .synopsis-panel {
    position: absolute;
    left: 0; top: 104px;
    width: 696px; height: 430px;
    background: var(--panel);
    border-top-right-radius: 34px;
  }
  .gold-rule {
    position: absolute;
    left: 100px; right: 0; top: 126px;
    height: 2px;
    background: linear-gradient(90deg, var(--gold), #e0c683 60%, var(--gold));
  }
  .mugshot {
    position: absolute;
    left: 134px; top: 10px;
    width: 158px; height: 108px;
    background: #f2eee6;
    padding: 7px;
    transform: rotate(-4deg);
    box-shadow: 0 3px 8px rgba(0,0,0,0.45);
  }
  .mugshot-fill {
    width: 100%; height: 100%;
    background: linear-gradient(90deg, #3a3a3a, #8a8a86 45%, #5b5b58 55%, #9b9a95);
  }
  .title {
    position: absolute;
    left: 310px; top: 14px;
    width: 200px;
    font-family: "Nunito", Arial, sans-serif;
    font-weight: 800;
    font-size: 21px;
    line-height: 1.12;
    color: var(--white);
    transform: rotate(-7deg);
    transform-origin: left top;
    text-shadow: 0 2px 4px rgba(0,0,0,0.5);
  }
  .logline {
    position: absolute;
    left: 536px; top: 18px;
    width: 512px;
    font-weight: 700;
    font-size: 14.4px;
    line-height: 1.3;
    color: var(--logline);
  }
  .stamp-box, .address-box, .barcode-box {
    position: absolute;
    background: var(--white);
    border: 1px solid var(--box-border);
    display: flex; align-items: center; justify-content: center;
    font-family: "Nunito Sans", Arial, sans-serif;
    color: var(--box-ink);
    letter-spacing: 0.5px;
  }
  .stamp-box { left: 1074px; top: 20px; width: 106px; height: 98px; font-size: 20px; }
  .address-box { left: 700px; top: 166px; width: 500px; height: 283px; font-size: 25px; }
  .barcode-box { left: 700px; top: 450px; width: 500px; height: 84px; font-size: 25px; }
  .synopsis-heading {
    position: absolute;
    left: 24px; top: 111px;
    font-size: 16px;
    font-weight: 600;
    color: var(--white);
  }
  .synopsis-body {
    position: absolute;
    left: 24px; top: 143px;
    width: 648px;
    font-size: 12.3px;
    line-height: 16.8px;
    color: var(--ink-light);
    text-align: justify;
  }
  .synopsis-body p { margin-bottom: 4px; }
</style>
</head>
<body>
  <div class="postcard">
    <div class="synopsis-panel"></div>
    <div class="gold-rule"></div>

    <div class="mugshot">
      <div class="mugshot-fill" role="img" aria-label="Vintage prison booking photograph of the young boy, profile and front views"></div>
    </div>

    <h1 class="title">A Lantern Under Frozen Water</h1>

    <p class="logline">In 1931, a 60-pound 12-year-old boy is sentenced to life in prison for murder. In this true story based on a book, the boy must learn how to navigate deadly politics amidst dangerous men and decide if becoming a savage is the way to become a man.</p>

    <div class="stamp-box">STAMP</div>

    <h2 class="synopsis-heading">Synopsis</h2>
    <div class="synopsis-body">
      <p>In this 1931 true story 12-year-old Tobias Wrenfield runs away from his abusive grandmother, breaks into the general store to get something to eat and is surprised in the act by the sheriff. Tobias fires a gun, accidentally kills the sheriff and is sentenced to life in an adult prison. He brings with him a beautiful blue marble, a souvenir of the summer skies of his childhood.</p>
      <p>As soon as Tobias gets to prison the power-hungry Guard Smedley puts him in a cell with Blu, an insane, homicidal pedophile. But Ray, a cunning con, comes to the naïve boy's aid. The no-nonsense Warden Ashgrove assigns Tobias to share a cell with Walter, a sullen 17-year-old, who becomes Tobias's closest friend. Ray continues to do Tobias favors and Walter cautions Tobias that Ray is not to be trusted.</p>
      <p>Harbor Hollow's Father Dunmore and a Seattle society woman, Odile Prescott, in the meantime, campaign to parole Tobias to Harbor Hollow, irritating the autocrat, Gov. Cyrus Whitmore, who will do anything to keep the boy in prison as a symbol of being tough on crime.</p>
      <p>In the meantime, Ray decides it is time to collect on the favors he has given to Tobias. Ray plans to escape and needs Tobias's help. Tobias agrees but when he realizes what he is asked to do will kill his friend, the prison librarian, he changes his mind. Just before the librarian drinks poison, Tobias knocks the cup away and blames Ray. Ray and his friends wait to get Tobias alone and plan to rape him.</p>
      <p>Walter hears Tobias scream and with mad-dog viciousness, Walter attacks Ray and his friends, killing one. Walter is sentenced to be executed and on the night of the hanging, Tobias escapes from his cell to try to save him. Tobias pleads with the warden to spare.</p>
    </div>

    <div class="address-box">ADDRESS AREA</div>
    <div class="barcode-box">BARCODE</div>
  </div>
</body>
</html>
```